A website for Medical Services to treat incontinence with a non-invasive product

We need to build a website to generate and convert new clients to schedule either treatment or book consultation (The device's name is QRV Floravia). Here are the reference sites for information only: (Please do not use the same style as this is the style we desperately want to change)
http://www.thepelvancenter.com/floravia-for-incontinence/
https://verdanomaktc.com/2018/04/13/urinary-incontinence/
https://verdanomaktc.com/non-invasive-lasers/female-incontinence/
http://www.drvorkin.com/services/wellness-services/sexual-health/qrv-floravia-urinary-incontinence-houston/

This is the vendor site:
https://corawellnex.com/

Target Market(s)

The targeted audience is mostly women between 30 - 75, suffering from stress incontinence due to childbirth and many other age-related conditions.

Industry/Entity Type

Health And Wellness

Number of Pages Required

4 page

Font styles to use
Sans Serif

Colors

Designer to choose colors to be used in the design.

Requirements
Must have
• How it works, How is it different from traditional invasive measures, What other people say about the treatment, video testimonials, FAQs, contact us, Book Appointment, latest promotions. maps, social media links
Nice to have
• The experienced urologist profile, office surroundings/interior, Reviews, number strips

```html
<!DOCTYPE html>
<html lang="en">
<head>
<meta charset="utf-8">
<title>QRV Floravia – Urine Incontinence Treatments</title>
<link href="https://fonts.googleapis.com/css2?family=Ubuntu:wght@300;400;500;700&display=swap" rel="stylesheet">
<style>
:root{
  --blue:#1c5390;
  --navy:#153e70;
  --red:#e11d2a;
  --dark:#333333;
  --strip:#3a3a3a;
  --text:#4a4a4a;
  --muted:#777;
  --hero-bg:#efefef;
  --pale:#dce7f1;
  --white:#ffffff;
}
*{margin:0;padding:0;box-sizing:border-box}
html,body{width:1200px;height:2857px;overflow:hidden}
body{position:relative;font-family:'Ubuntu',sans-serif;color:var(--text);background:var(--white)}
.abs{position:absolute}

/* top bar */
.topbar{left:0;top:0;width:1200px;height:38px;background:var(--blue)}
.social{left:99px;top:11px;display:flex;gap:10px}
.social span{width:15px;height:15px;border-radius:50%;background:var(--white);opacity:.9}
.pill{top:5px;height:28px;border:1.5px solid var(--white);border-radius:14px;color:var(--white);font-size:13px;display:flex;align-items:center;justify-content:center;gap:8px;white-space:nowrap}
.pill.phone{left:642px;width:152px}
.pill.mail{left:813px;width:136px}
.pill.provider{left:964px;width:137px;background:var(--red);border-color:var(--red);font-size:14px}

/* nav */
.logo{left:99px;top:56px;display:flex;align-items:center;gap:10px}
.logo .mark{width:34px;height:34px;background:var(--blue)}
.logo .name{font-size:26px;font-weight:700;color:var(--blue)}
.nav{right:99px;top:72px;display:flex;gap:26px;font-size:13px;color:var(--navy)}

/* hero */
.hero{left:0;top:120px;width:1200px;height:512px;background:var(--hero-bg)}
.hero-photo{left:438px;top:120px;width:762px;height:512px;background:linear-gradient(90deg,var(--hero-bg) 0%,#ebe6e2 25%,#e2cfc3 55%,#f3f1ee 100%)}
.hero-title{left:99px;top:268px;font-size:30px;font-weight:700;color:var(--red)}
.hero-sub{left:101px;top:314px;font-size:22px;color:var(--blue)}
.hero-sub b{font-size:34px;font-weight:400}
.hero-text{left:104px;top:360px;width:490px;font-size:12.5px;line-height:17px;color:var(--text)}
.btn{height:38px;border-radius:19px;background:var(--blue);color:var(--white);font-size:14px;display:flex;align-items:center;justify-content:center;box-shadow:0 2px 0 var(--navy)}
.btn.appt{left:99px;top:439px;width:156px}
.btn.services{left:265px;top:439px;width:158px}

/* how it works */
.section-title{left:0;width:1200px;text-align:center;font-size:26px;font-weight:700;color:#222}
.hiw-title{top:699px}
.hiw-text{left:181px;top:748px;width:838px;text-align:center;font-size:12.5px;line-height:24px}
.step{width:180px;text-align:center}
.step .ring{width:108px;height:108px;margin:0 auto;border-radius:50%;border:1px solid #dcdcdc;background:var(--white);display:flex;align-items:center;justify-content:center}
.step h3{font-size:16px;font-weight:400;color:var(--navy);margin-top:12px;line-height:20px}
.step p{font-size:12.5px;line-height:20px;margin-top:12px;padding:0 12px}

/* why choose / different */
.band{left:0;top:1452px;width:1200px;height:525px;background:linear-gradient(120deg,#1d5492 0%,#1a4c86 50%,#2a6aa8 80%,#17457c 100%)}
.why-box{left:99px;top:1320px;width:495px;height:543px;background:var(--dark)}
.why-rule{left:118px;top:1358px;width:48px;height:2px;background:var(--white)}
.why-title{left:118px;top:1375px;font-size:20px;color:var(--white)}
.doctor-photo{left:118px;top:1430px;width:220px;height:400px;background:linear-gradient(180deg,#4b4b4b 0%,#2a2a2a 55%,#cfd3d6 80%,#8e9398 100%)}
.quote-mark{left:322px;top:1400px;font-size:110px;color:#8a8a8a;font-family:Georgia,serif;line-height:1}
.quote{left:347px;top:1446px;width:220px;font-size:13px;line-height:24.5px;color:var(--white)}
.quote-name{left:347px;top:1670px;font-size:13px;color:var(--white)}
.quote-name b{font-weight:700}
.diff-title{left:625px;top:1478px;font-size:27px;font-weight:300;line-height:37px;color:var(--white)}
.list{list-style:none;font-size:13px;line-height:36px}
.list li{position:relative;padding-left:18px}
.list li::before{content:"";position:absolute;left:0;top:15px;width:6px;height:6px;border-radius:50%;background:currentColor}
.diff-list{top:1561px;color:var(--white)}
.diff-list.c1{left:625px}.diff-list.c2{left:892px}
.featured{left:625px;top:1836px;font-size:26px;font-weight:300;color:var(--white)}
.badge{top:1890px;height:36px;border:1.5px solid rgba(255,255,255,.75);border-radius:4px}

/* contact strip */
.strip{left:0;top:1977px;width:1200px;height:99px;background:var(--strip)}
.contact-item{top:2015px;font-size:20px;color:var(--white);display:flex;align-items:center;gap:10px;white-space:nowrap}

/* say no */
.sayno-rule{left:576px;top:2130px;width:48px;height:2px;background:#bbb}
.sayno-title{top:2154px}
.sayno-text{left:99px;top:2230px;width:475px;font-size:12.5px;line-height:37px}
.sayno-list{top:2220px;color:var(--navy)}
.sayno-list li{color:var(--text)}
.sayno-list li::before{background:var(--navy)}
.sayno-list.c1{left:640px}.sayno-list.c2{left:899px}
.btn.meet{left:99px;top:2393px;width:151px}
.features{left:99px;top:2486px;width:1002px;height:191px;border:1px solid #e2e2e2;display:flex}
.feature{flex:1;border-right:1px solid #e2e2e2;display:flex;flex-direction:column;align-items:center;padding-top:40px}
.feature:last-child{border-right:none}
.feature span{margin-top:22px;font-size:14px;color:var(--text)}

/* appointment */
.appt-band{left:0;top:2758px;width:1200px;height:99px;background:var(--pale)}
.appt-rule{left:712px;top:2811px;width:46px;height:2px;background:var(--navy)}
.appt-title{left:712px;top:2824px;font-size:27px;color:var(--navy)}
</style>
</head>
<body>

<div class="abs topbar"></div>
<div class="abs social" aria-label="Social media links"><span></span><span></span><span></span><span></span><span></span></div>
<div class="abs pill phone">
  <svg width="13" height="13" viewBox="0 0 24 24"><path fill="#fff" d="M6.6 10.8a15 15 0 0 0 6.6 6.6l2.2-2.2c.3-.3.7-.4 1-.2 1.1.4 2.3.6 3.6.6.6 0 1 .4 1 1V20c0 .6-.4 1-1 1A17 17 0 0 1 3 4c0-.6.4-1 1-1h3.5c.6 0 1 .4 1 1 0 1.3.2 2.5.6 3.6.1.3 0 .7-.2 1z"/></svg>
  0800 314 2718
</div>
<div class="abs pill mail">
  <svg width="13" height="11" viewBox="0 0 24 18"><rect x="1" y="1" width="22" height="16" rx="2" fill="none" stroke="#fff" stroke-width="2"/><path d="M1 2l11 8 11-8" fill="none" stroke="#fff" stroke-width="2"/></svg>
  <span style="font-size:11px">info@qrvfloravia.com</span>
</div>
<div class="abs pill provider">Find a Provider</div>

<header>
  <div class="abs logo"><span class="mark"></span><span class="name">QRV Floravia</span></div>
  <nav class="abs nav"><span>Products</span><span>Events</span><span>Education Center</span><span>Media</span><span>News</span><span>About</span><span>Contact</span><span>QRV Support</span></nav>
</header>

<section>
  <div class="abs hero"></div>
  <div class="abs hero-photo" role="img" aria-label="Photo of a woman in white clothing holding her lower abdomen"></div>
  <h1 class="abs hero-title">URINE INCONTINENCE TREATMENTS</h1>
  <p class="abs hero-sub">We <b>Guarantee</b> you, the best &nbsp;change in you</p>
  <p class="abs hero-text">Lorem ipsum dolor sit amet, consectetur adipiscing elit. Phasellus augue nibh, cursus eu commodo nec, vulputate sed justo. Morbi elementum arcu ultricies iaculis sodales.</p>
  <a class="abs btn appt">Fix an Appointment</a>
  <a class="abs btn services">View Services</a>
</section>

<section>
  <h2 class="abs section-title hiw-title">HOW IT WORKS</h2>
  <p class="abs hiw-text">Lorem ipsum dolor sit amet, consectetur adipiscing elit. Sed varius egestas nisl quis imperdiet. Integer quis sapien ultrices, posuere velit sit amet, aliquet tortor. Morbi auctor quam eu nulla tincidunt facilisis. Aliquam massa enim, egestas tincidunt consequat i</p>
  <svg class="abs" style="left:0;top:820px" width="1200" height="240" viewBox="0 0 1200 240">
    <g fill="none" stroke="#9a9a9a" stroke-width="1.5" stroke-dasharray="2 5">
      <path d="M318 60 Q400 70 420 165"/>
      <path d="M466 165 Q480 70 540 60"/>
      <path d="M642 60 Q740 70 760 165"/>
      <path d="M800 165 Q820 70 880 60"/>
    </g>
  </svg>

  <div class="abs step" style="left:175px;top:826px">
    <div class="ring"><svg width="56" height="56" viewBox="0 0 56 56" fill="none" stroke="#1c5390" stroke-width="4" stroke-linecap="round"><path d="M12 6v14a10 10 0 0 0 20 0V6"/><path d="M22 30v8a10 10 0 0 0 20 0v-6"/><circle cx="42" cy="26" r="5"/></svg></div>
    <h3>Diagnose</h3>
    <p>Lorem ipsum dolor sit amet, consectetur adipisc-ing elit. Praesent ultrice s,</p>
  </div>
  <div class="abs step" style="left:342px;top:984px">
    <div class="ring"><svg width="60" height="60" viewBox="0 0 60 60"><circle cx="30" cy="30" r="28" fill="#1c5390"/><circle cx="30" cy="30" r="17" fill="none" stroke="#fff" stroke-width="3"/><circle cx="26" cy="26" r="4" fill="#fff"/><circle cx="35" cy="32" r="3" fill="#fff"/></svg></div>
    <h3>Absorbent<br>Products</h3>
    <p>Lorem ipsum dolor sit amet, consectetur adipisc-ing elit. Praesent ultrice s,</p>
  </div>
  <div class="abs step" style="left:509px;top:826px">
    <div class="ring"><svg width="40" height="60" viewBox="0 0 40 60" fill="none" stroke="#1c5390" stroke-width="3"><path d="M20 2v8"/><rect x="6" y="10" width="28" height="38" rx="10"/><path d="M20 20v14"/><path d="M20 48v10"/></svg></div>
    <h3>Handheld<br>Urinals</h3>
    <p>Lorem ipsum dolor sit amet, consectetur adipisc-ing elit. Praesent ultrice s,</p>
  </div>
  <div class="abs step" style="left:676px;top:984px">
    <div class="ring"><svg width="50" height="54" viewBox="0 0 50 54"><rect x="4" y="2" width="42" height="10" fill="#1c5390"/><path d="M8 14h34l-4 38H12z" fill="#1c5390"/><rect x="16" y="24" width="18" height="14" fill="none" stroke="#fff" stroke-width="3"/></svg></div>
    <h3>A catheter</h3>
    <p>Lorem ipsum dolor sit amet, consectetur adipisc-ing elit. Praesent ultrice s,</p>
  </div>
  <div class="abs step" style="left:843px;top:826px">
    <div class="ring"><svg width="40" height="60" viewBox="0 0 40 60" fill="#1c5390"><circle cx="20" cy="8" r="6"/><path d="M10 18h20l-4 18 4 22h-6l-4-18-4 18h-6l4-22z"/></svg></div>
    <h3>Prevent urine<br>leakage</h3>
    <p>Lorem ipsum dolor sit amet, consectetur adipisc-ing elit. Praesent ultrice s,</p>
  </div>
</section>

<section>
  <div class="abs band" role="img" aria-label="Blue tinted photo of a treatment room"></div>
  <div class="abs why-box"></div>
  <div class="abs why-rule"></div>
  <h2 class="abs why-title">WHY CHOOSE US</h2>
  <div class="abs doctor-photo" role="img" aria-label="Photo of the physician seated on the treatment chair"></div>
  <div class="abs quote-mark">“</div>
  <p class="abs quote">Lorem ipsum dolor sit amet, con-sectetur adipiscing elit. Nam vitae tortor eget nisi consequat hendre-rit. Fusce eros nibh, sagittis ac tortor a, consequat blandit metus. Suspendisse et mi ullamcorper, luctus ipsum eu, lobortis nibh.</p>
  <p class="abs quote-name"><b>Marisol Denhart</b> M.D, F.A.C.S.</p>

  <h2 class="abs diff-title">HOW IS IT DIFFERENT FROM<br>TRADITIONAL INVASIVE MEASURES</h2>
  <ul class="abs list diff-list c1"><li>Sed rhoncus, nisi ac commodo</li><li>Blandit metus lorem egestas</li><li>Orci &nbsp;nec elementum enim</li><li>Tellus sit amet felis aecenas in</li><li>Ultricies sem &nbsp;pellentesque</li><li>Turpis felis &nbsp;sagittis ut libero</li><li>Gravida porta arcu</li></ul>
  <ul class="abs list diff-list c2"><li>Sed rhoncus, nisi ac commodo</li><li>Blandit metus lorem egestas</li><li>Orci &nbsp;nec elementum enim</li><li>Tellus sit amet felis aecenas in</li><li>Ultricies sem &nbsp;pellentesque</li><li>Turpis felis &nbsp;sagittis ut libero</li><li>Gravida porta arcu</li></ul>
  <h3 class="abs featured">As Featured In</h3>
  <div class="abs badge" style="left:625px;width:140px"></div>
  <div class="abs badge" style="left:785px;width:160px"></div>
  <div class="abs badge" style="left:970px;width:130px"></div>
</section>

<section>
  <div class="abs strip"></div>
  <div class="abs contact-item" style="left:99px">
    <svg width="20" height="20" viewBox="0 0 24 24"><path fill="#fff" d="M6.6 10.8a15 15 0 0 0 6.6 6.6l2.2-2.2c.3-.3.7-.4 1-.2 1.1.4 2.3.6 3.6.6.6 0 1 .4 1 1V20c0 .6-.4 1-1 1A17 17 0 0 1 3 4c0-.6.4-1 1-1h3.5c.6 0 1 .4 1 1 0 1.3.2 2.5.6 3.6.1.3 0 .7-.2 1z"/></svg>
    0800 314 2718</div>
  <div class="abs contact-item" style="left:358px">
    <svg width="22" height="16" viewBox="0 0 24 18"><rect width="24" height="18" rx="2" fill="#fff"/><path d="M1 2l11 8 11-8" fill="none" stroke="#3a3a3a" stroke-width="2"/></svg>
    info@qrvfloravia.com</div>
  <div class="abs contact-item" style="left:631px">
    <svg width="16" height="22" viewBox="0 0 16 22"><path fill="#fff" d="M8 0a8 8 0 0 1 8 8c0 6-8 14-8 14S0 14 0 8a8 8 0 0 1 8-8z"/><circle cx="8" cy="8" r="3" fill="#3a3a3a"/></svg>
    27 Marlowe Crescent, Fenwick Vale 40219</div>
</section>

<section>
  <div class="abs sayno-rule"></div>
  <h2 class="abs section-title sayno-title">SAY NO TO INCONTINENCE</h2>
  <p class="abs sayno-text">Duas molestias excepturi sint occaecati cupiditate non provident, similique sunt in culpa qui officia deserunt mollitia animi, id est laborum et dolorum. Et harum quidem rerum facilis est et expeditturation. Duas molestias excepturi sint occaecati cupiditate</p>
  <ul class="abs list sayno-list c1"><li>Nunc gravida imperdiet</li><li>Duis mauris nibh, tempus</li><li>Pellentesque fermen tum</li><li>Cras lacinia, augue sed finibus</li><li>Volutpat, arcu arcu euismod</li></ul>
  <ul class="abs list sayno-list c2"><li>Nunc gravida imperdiet</li><li>Duis mauris nibh, tempus</li><li>Pellentesque fermen tum</li><li>Cras lacinia, augue sed finibus</li><li>Volutpat, arcu arcu euismod</li></ul>
  <a class="abs btn meet">Meet Dr. Halvern</a>

  <div class="abs features">
    <div class="feature">
      <svg width="70" height="70" viewBox="0 0 70 70" fill="none" stroke="#1c5390" stroke-width="3"><circle cx="35" cy="35" r="32"/><rect x="20" y="26" width="30" height="16" rx="8" transform="rotate(-40 35 34)"/><path d="M12 12l46 46"/></svg>
      <span>Drug Free</span></div>
    <div class="feature">
      <svg width="70" height="70" viewBox="0 0 70 70" fill="#1c5390"><path d="M8 8l38 38-6 6L4 14z"/><path d="M62 8L24 46l6 6 36-38z"/><circle cx="14" cy="58" r="7"/><circle cx="56" cy="58" r="7"/></svg>
      <span>Surgery Free</span></div>
    <div class="feature">
      <svg width="70" height="70" viewBox="0 0 70 70" fill="#1c5390"><circle cx="35" cy="14" r="12"/><circle cx="12" cy="38" r="11"/><circle cx="58" cy="38" r="11"/><path d="M22 30h26l-6 36H28z"/></svg>
      <span>Totally Non-invasive</span></div>
    <div class="feature">
      <svg width="70" height="70" viewBox="0 0 70 70" fill="none" stroke="#1c5390" stroke-width="4"><circle cx="35" cy="38" r="26"/><path d="M35 22v17l10 8"/><path d="M28 6h14M35 6v6"/></svg>
      <span>Long Lasting</span></div>
  </div>
</section>

<section>
  <div class="abs appt-band"></div>
  <div class="abs appt-rule"></div>
  <h2 class="abs appt-title">FIX AN APPOINTMENT</h2>
</section>

</body>
</html>
```